Additional Benefits of Working for VALMIRA

Please prepare an infographic on the additional benefits besides salary of working at VALMIRA as detailed in the attached word document. Also attached is our logo in eps and our company design "Grounds". We are a Not For Profit company that finds jobs for unemployed people of government benefit payments

Homefield Market(s)

Attracting people to work for VALMIRA. Making VALMIRA an employer of choice.

Font styles to use
Sans Serif

Colors

Designer to choose colors to be used in the design.

Requirements
Must have
• be on 1 page
• have our logo
Nice to have
• Our Grounds design worked into it.
• Happy engaged employees
• Community engagement - we are a not for profit organisation
Should not have
• Discrimination, swearing,

```html
<!DOCTYPE html>
<html lang="en">
<head>
<meta charset="utf-8">
<title>The Benefits of Working with Us – VALMIRA</title>
<link rel="stylesheet" href="https://fonts.googleapis.com/css2?family=Marcellus&family=Noto+Sans:wght@400;500&display=swap">
<style>
  :root {
    --band: #86b43c;
    --band-light: #8cc443;
    --card: #dde9c2;
    --rule: #93bd4f;
    --bullet: #7fbd3a;
    --ink: #14241a;
    --white: #ffffff;
  }
  * { box-sizing: border-box; margin: 0; padding: 0; }
  html, body { width: 1200px; height: 1190px; overflow: hidden; background: var(--white); }
  .canvas { position: relative; width: 1200px; height: 1190px; overflow: hidden; background: var(--white); font-family: "Noto Sans", Verdana, sans-serif; color: var(--ink); }

  .title-band { position: absolute; left: 70px; top: 22px; width: 1080px; height: 115px; background: var(--band); }
  .title-band svg { position: absolute; left: 0; top: 0; }
  .title { position: absolute; left: 0; right: 0; top: 18px; text-align: center; font-family: "Marcellus", serif; font-size: 62px; font-weight: 400; letter-spacing: 0.5px; -webkit-text-stroke: 2px var(--ink); color: var(--ink); white-space: nowrap; }

  .row-band { position: absolute; left: 70px; top: 682px; width: 1080px; height: 14px; background: var(--band); }

  .card { position: absolute; width: 260px; background: var(--card); border-left: 2px solid var(--rule); border-right: 2px solid var(--rule); border-bottom: 2px solid var(--rule); border-radius: 0 0 48px 48px; }
  .card.square-left { border-bottom-left-radius: 0; }
  .card.square-right { border-bottom-right-radius: 0; }
  .top { top: 136px; height: 527px; }
  .bottom { top: 696px; height: 456px; }
  .c1 { left: 70px; } .c2 { left: 345px; } .c3 { left: 618px; } .c4 { left: 890px; }

  .card-head { height: 71px; display: flex; align-items: center; justify-content: center; text-align: center; font-family: "Marcellus", serif; font-weight: 400; font-size: 25px; line-height: 1.12; border-bottom: 3px solid var(--rule); position: relative; padding: 0 8px; }
  .card-head.small { font-size: 17px; }
  .card-head.mid { font-size: 22px; }
  .card-head::after { content: ""; position: absolute; left: 50%; bottom: -5px; width: 7px; height: 7px; margin-left: -3.5px; border-radius: 50%; background: var(--rule); }

  .perks { list-style: none; padding: 22px 6px 0 8px; }
  .perks li { position: relative; padding-left: 20px; font-size: 17.5px; font-weight: 500; letter-spacing: 0.6px; line-height: 21.5px; margin-bottom: 19px; }
  .perks li::before { content: ""; position: absolute; left: 0; top: 3px; border-left: 14px solid var(--bullet); border-top: 8px solid transparent; border-bottom: 8px solid transparent; }

  .brand-tile { position: absolute; left: 996px; top: 1036px; width: 220px; height: 170px; background: var(--white); border-top-left-radius: 48px; display: flex; align-items: center; justify-content: center; padding-right: 16px; }
  .brand-name { font-family: "Noto Sans", Verdana, sans-serif; font-weight: 500; font-size: 38px; color: var(--ink); letter-spacing: -0.5px; }
</style>
</head>
<body>
<main class="canvas">
  <header class="title-band">
    <svg width="1080" height="115" viewBox="0 0 1080 115" aria-hidden="true">
      <path d="M60 14 H1068 Q1058 80 980 100 H14 Q20 30 60 14 Z" fill="var(--band-light)"/>
    </svg>
    <h1 class="title">The Benefits of Working with Us</h1>
  </header>

  <section class="card top c1 square-left">
    <h2 class="card-head">Life Balance</h2>
    <ul class="perks">
      <li>VALMIRA Day Leave. An extra day off at Christmas!</li>
      <li>Birthday Leave. A paid day off on your birthday</li>
      <li>A day off every month as Time in Lieu</li>
      <li>4 weeks Annual Leave</li>
      <li>Generous Personal Leave</li>
      <li>Support for parental leave for the birth or adoption of a child</li>
      <li>Flexible work arrangements</li>
    </ul>
  </section>

  <section class="card top c2">
    <h2 class="card-head">Wellbeing</h2>
    <ul class="perks">
      <li>Up to $450 per year to spend on Wellbeing services such as gym or yoga memberships</li>
      <li>Free counselling services 24x7 via our Employee Assistance Program</li>
      <li>Discount private health insurance</li>
      <li>WHS policies which support a safe, inclusive work place</li>
    </ul>
  </section>

  <section class="card top c3">
    <h2 class="card-head small">Career Growth &amp;<br>Professional Development</h2>
    <ul class="perks">
      <li>Ongoing internal training and development opportunities.</li>
      <li>External study support &amp; study leave</li>
      <li>Access to the tools and technology to do your job well</li>
      <li>Career advancement opportunities</li>
      <li>Internal job vacancy listings</li>
    </ul>
  </section>

  <section class="card top c4 square-right">
    <h2 class="card-head mid">Remuneration &amp;<br>Salary Packaging</h2>
    <ul class="perks">
      <li>Competitive salary</li>
      <li>Ability to salary package up to $15,900 and reduce your tax. Package rent, home loans, child care and much more</li>
      <li>Salary package up to $2,650 on meal entertainment and holiday accommodation</li>
    </ul>
  </section>

  <div class="row-band"></div>

  <section class="card bottom c1 square-left">
    <h2 class="card-head">Benefits</h2>
    <ul class="perks">
      <li>Discounted vouches for Pantrywise, Greengate’s, Voltro, Reelhouse, Cellar Lane, Norbay, Homefield, Outpost and many others via Tessa e-wallet</li>
      <li>A range of other employee discounts are also available, including access to discounted banking and finance, vehicle purchasing, leasing and hotel accommodation</li>
    </ul>
  </section>

  <section class="card bottom c2">
    <h2 class="card-head">Contributing<br>to Community</h2>
    <ul class="perks">
      <li>Team involvement in local charity and community events</li>
      <li>Participation in VALMIRA’s 1000 Jobs in 100 days initiative</li>
      <li>Strong relationships and connection with Indigenous Communities in support of Indigenous Employment</li>
    </ul>
  </section>

  <section class="card bottom c3">
    <h2 class="card-head">Recognition</h2>
    <ul class="perks">
      <li>We celebrate our people for reaching service milestones</li>
      <li>Team &amp; individual recognition for high performance</li>
    </ul>
  </section>

  <section class="card bottom c4 square-right">
    <h2 class="card-head">Diversity &amp;<br>Inclusion</h2>
    <ul class="perks">
      <li>An inclusive and diverse culture where different backgrounds, experiences and perspectives are valued</li>
      <li>Gender diversity. Over 50% of our workforce and our leaders are female.</li>
    </ul>
  </section>

  <div class="brand-tile">
    <span class="brand-name">valmira</span>
  </div>
</main>
</body>
</html>
```